Chimney Service company needs new business card design

We need a updated business card with our new logo added. We provide a full range of chimney services throughout Vermont and New Hampshire. The business card will be one sided and color. Attached is our current business card another document showing all the information we would like on the card.
We dont like a lot of flashy colors.... here is a link to our website to get an idea of our branding www.flueguardianvt.example

Target Market(s)

homeowners

Industry/Entity Type

Business

Contact Information for Business Card

See attached sheet for content.

Font styles to use
Serif
Sans Serif

Requirements
Must have
• all information provided on separate sheet
Should not have
• Additional information that may clogg up design

```html
<!DOCTYPE html>
<html lang="en">
<head>
<meta charset="utf-8">
<title>Flue Guardian – Business Card</title>
<link rel="stylesheet" href="https://fonts.googleapis.com/css2?family=Cabin:ital,wght@0,400;0,500;1,400&display=swap">
<style>
  :root {
    --page-bg: #a9aaad;
    --card-bg: #ffffff;
    --ink: #2b2b2b;
    --brand-red: #941a1d;
    --band-dark: #2b2b2b;
    --on-band: #ffffff;
  }
  html, body {
    margin: 0;
    width: 1200px;
    height: 1000px;
    overflow: hidden;
    background: var(--page-bg);
    font-family: "Cabin", "Gill Sans", sans-serif;
  }
  .card {
    position: absolute;
    left: 252px;
    top: 279px;
    width: 696px;
    height: 442px;
    background: var(--card-bg);
  }
  .brand {
    position: absolute;
    left: 40px;
    top: 112px;
    width: 235px;
    display: flex;
    align-items: center;
    justify-content: center;
    gap: 10px;
  }
  .brand-mark {
    width: 14px;
    height: 14px;
    background: var(--brand-red);
  }
  .brand-name {
    font-size: 22px;
    font-weight: 500;
    letter-spacing: 0.5px;
    color: var(--ink);
    text-transform: uppercase;
  }
  .service-area {
    position: absolute;
    left: 40px;
    top: 177px;
    width: 225px;
    text-align: center;
    font-style: italic;
    font-size: 16.5px;
    line-height: 22px;
    color: var(--brand-red);
  }
  .contact {
    position: absolute;
    left: 28px;
    top: 311px;
    margin: 0;
    padding: 0;
    list-style: none;
  }
  .contact li {
    display: flex;
    align-items: center;
    height: 37px;
    font-size: 21px;
    letter-spacing: 0.3px;
    color: var(--ink);
  }
  .contact svg {
    width: 18px;
    height: 18px;
    margin-right: 7px;
    flex: none;
  }
  .band {
    position: absolute;
    left: 335px;
    width: 361px;
    margin: 0;
    padding: 0;
    list-style: none;
  }
  .band li {
    position: relative;
    padding-left: 20px;
    font-size: 19.5px;
    color: var(--on-band);
    height: 31.3px;
    line-height: 31px;
  }
  .band li::before,
  .band li::after {
    content: "";
    position: absolute;
    top: 11px;
    width: 9px;
    height: 8px;
  }
  .band li::before { left: -9px; }
  .band li::after { left: 0; background: var(--on-band); }
  .band-promise {
    top: 98px;
    height: 71px;
    padding-top: 3px;
    box-sizing: border-box;
    background: var(--band-dark);
  }
  .band-promise li::before { background: var(--brand-red); }
  .band-services {
    top: 172px;
    height: 171px;
    padding-top: 5px;
    box-sizing: border-box;
    background: var(--brand-red);
  }
  .band-services li::before { background: var(--band-dark); }
</style>
</head>
<body>
  <div class="card">
    <div class="brand">
      <span class="brand-mark"></span>
      <span class="brand-name">Flue Guardian</span>
    </div>

    <p class="service-area">Serving VT &amp; New Hampshire<br>since 1989</p>

    <ul class="contact">
      <li>
        <svg viewBox="0 0 20 20" aria-hidden="true"><circle cx="10" cy="10" r="10" fill="#941a1d"/><path d="M6.5 5h2l1 2.6-1.3 1a6 6 0 0 0 3.2 3.2l1-1.3 2.6 1v2c0 .6-.5 1-1 1A9 9 0 0 1 5.5 6c0-.5.4-1 1-1z" fill="#fff"/></svg>
        802-555-0147
      </li>
      <li>
        <svg viewBox="0 0 20 20" aria-hidden="true"><circle cx="10" cy="10" r="10" fill="#941a1d"/><text x="10" y="14" text-anchor="middle" font-size="12" font-family="Cabin, sans-serif" fill="#fff">@</text></svg>
        info@flueguardianvt.example
      </li>
      <li>
        <svg viewBox="0 0 20 20" aria-hidden="true"><circle cx="10" cy="10" r="10" fill="#941a1d"/><g fill="none" stroke="#fff" stroke-width="1"><circle cx="10" cy="10" r="6"/><ellipse cx="10" cy="10" rx="2.6" ry="6"/><path d="M4 10h12M5 7h10M5 13h10"/></g></svg>
        www.flueguardianvt.example
      </li>
    </ul>

    <ul class="band band-promise">
      <li>Fully Insured – Free Estimates</li>
      <li>Family owned &amp; operated</li>
    </ul>

    <ul class="band band-services">
      <li>Full Masonry Services</li>
      <li>Historic Chimney Restoration</li>
      <li>Stainless Steel Liners</li>
      <li>New Chimney Installations</li>
      <li>HCSG Certified Chimney Sweeps</li>
    </ul>
  </div>
</body>
</html>
```